Education portal needs a new Email Creative Design

We could not decide on the creative earlier as we were unable to picture how will it look. Hence, we have added content so that we can choose the best design of all. Below is the content to be used for the email creative:
____________________________________
Did you know that 25% of all Americans have experienced at least one divorce?*
41% of first marriages end in divorce!!*

Over 1 million children are affected by divorce each year*

Become a Marriage and Family therapist - Achieve inner-happiness by helping individuals, families and couples resolve their struggles and enhance their lives.
Family Therapists are trained in various modes of therapy in order to prepare them for work with individuals, families, couples, and groups.

With proper training, you will be able to treat:
• Depression and other Affective Disorders
• Childhood Behavioral and Emotional Disorders
• Marital and Relationship Problems
• Conduct Disorder and Delinquency
• Substance Abuse
• Alcoholism
• Domestic Violence
• Severe Mental Illness
• Physical Illness

You could also qualify for financial aid* from the government to pursue this career..

Secure your life by earning upto $78,580* and attain peace of mind while helping others..

__________________________

These are the links to images we liked, but if you have something better, we would love to see them:
http://www.pexalunto.com/photo/seperated-58301947?st=7bk2913
http://www.pexalunto.com/photo/domestic-violence-72950386?st=f84m615

We are an education portal offering options of schools, colleges, universities and courses to students and working professionals.

We are looking for an email creative which has great call-to-action; be creative and research more if you wish.
Incorporate call-to-action tabs, make it colorful, include pictures and content.
Also attached are industry standard creatives for your reference, let me know if you have any questions.

Please see new files uploaded

I have uploaded a new creative made by our design team. Follow similar guidelines

For those who have not submitted their designs, please send us soon. Thanks

We thought a content brief will do more justice to this design contest hence we have updated our brief with new content to create a newer design Please submit your designs soon. Thanks

Target Market(s)

25 to 50 years working professionals

Industry/Entity Type

Government

Font styles to use
Serif
Sans Serif
Decorative
Script

Requirements
Must have
• Call-to-action

```html
<!DOCTYPE html>
<html lang="en">
<head>
<meta charset="utf-8">
<title>Become a Marriage and Family Therapist</title>
<link rel="stylesheet" href="https://fonts.googleapis.com/css2?family=Arimo:ital,wght@0,400;0,700;1,400&family=Roboto+Condensed:wght@700&display=swap">
<style>
  :root {
    --page: #ffffff;
    --ink: #151515;
    --pink: #c2286c;
    --pink-dark: #8e1447;
    --pink-light: #d2417f;
    --panel-pink: #b4285f;
    --blue-head: #3f78b6;
    --blue-light: #63b6da;
    --blue-deep: #3a6fb5;
    --tab-top: #3cb4ef;
    --tab-bottom: #1686cf;
    --white: #ffffff;
    --band: #f1f1f1;
    --brand: #f4e61c;
  }
  * { margin: 0; padding: 0; box-sizing: border-box; }
  html, body { width: 900px; height: 1200px; overflow: hidden; background: var(--page); }
  .canvas { position: relative; width: 900px; height: 1200px; font-family: "Arimo", Arial, sans-serif; }
  .email { position: absolute; left: 92px; top: 48px; width: 718px; height: 1103px; overflow: hidden;
    background: linear-gradient(120deg, var(--blue-light) 0%, #4f96cc 55%, var(--blue-deep) 100%); }
  .hero-photo { position: absolute; left: 0; top: 0; width: 718px; height: 475px;
    background: radial-gradient(ellipse at 52% 40%, #e4f4ec 0%, #b9dcd8 40%, #7fa7b6 100%); }
  .stats { position: absolute; left: 270px; width: 200px; text-align: center; font-weight: 700;
    font-size: 15px; line-height: 17px; color: var(--ink); text-transform: uppercase; }
  .stats em { font-style: normal; color: var(--pink); }
  .stat-one { top: 84px; }
  .stat-two { top: 221px; }
  .stat-three { top: 340px; }
  .ribbon { position: absolute; left: 0; top: 395px; }
  .kicker { position: absolute; left: 26px; top: 502px; font-style: italic; font-size: 24px; color: var(--pink); }
  .headline { position: absolute; left: 22px; top: 520px; font-family: "Roboto Condensed", Arial, sans-serif;
    font-weight: 700; font-size: 84px; line-height: 100px; color: var(--blue-head); letter-spacing: 1px; }
  .intro { position: absolute; left: 28px; top: 666px; width: 680px; font-size: 15.5px; line-height: 20px; color: var(--white); }
  .treat-panel { position: absolute; left: 24px; top: 752px; width: 673px; height: 235px; background: var(--panel-pink); }
  .cta-tab { position: absolute; left: 170px; top: 745px; width: 356px; height: 52px; }
  .cta-label { position: absolute; left: 268px; top: 754px; font-family: "Roboto Condensed", Arial, sans-serif;
    font-weight: 700; font-size: 29px; color: var(--white); }
  .treat-title { position: absolute; left: 44px; top: 828px; font-family: "Roboto Condensed", Arial, sans-serif;
    font-weight: 700; font-size: 19px; color: var(--white); }
  .conditions { position: absolute; top: 866px; list-style: none; font-size: 13.5px; line-height: 22.5px; color: var(--white); }
  .conditions li::before { content: "\2022\00a0"; }
  .conditions-left { left: 50px; }
  .conditions-right { left: 504px; }
  .tail { position: absolute; left: 40px; top: 987px; }
  .aid-note { position: absolute; left: 146px; top: 1007px; font-size: 13px; line-height: 15.5px; color: var(--white); letter-spacing: 0.3px; }
  .aid-note strong { color: var(--pink); font-size: 15px; }
  .brand { position: absolute; left: 530px; top: 1035px; font-size: 20px; color: var(--brand); }
</style>
</head>
<body>
<div class="canvas">
  <div class="email">
    <div class="hero-photo" role="img" aria-label="Photo of a mother and two children standing on a cliff edge, separated by a gap from a father on the opposite cliff"></div>

    <p class="stats stat-one">Did you know that <em>25%</em> of all Americans have experienced at least <em>one divorce?*</em></p>
    <p class="stats stat-two"><em>41%</em> of first marriages <em>end in divorce!!*</em></p>
    <p class="stats stat-three">Over <em>1 million</em> children are affected <em>by divorce each year*</em></p>

    <svg class="ribbon" width="718" height="260" viewBox="0 0 718 260" aria-hidden="true">
      <polygon points="80,75 560,40 560,120 80,120" fill="var(--pink-dark)"/>
      <polygon points="0,70 555,115 580,220 0,220" fill="var(--band)"/>
      <polygon points="0,222 580,222 668,245 0,248" fill="var(--pink-dark)"/>
      <polygon points="555,80 718,0 718,155 555,150" fill="var(--pink)"/>
      <polygon points="600,10 718,0 718,90" fill="var(--pink-light)"/>
      <polygon points="555,150 718,155 640,245" fill="var(--pink-light)"/>
      <polygon points="580,220 640,245 668,245 600,198" fill="var(--pink-dark)"/>
    </svg>

    <p class="kicker">Become a Marriage and Family</p>
    <h1 class="headline">THERAPIST</h1>

    <p class="intro">Achieve inner-happiness by helping individuals, families and couples resolve their struggles and enhance their lives. Family Therapists are trained in various modes of therapy in order to prepare them for work with individuals, families, couples, and groups.</p>

    <div class="treat-panel"></div>
    <svg class="cta-tab" viewBox="0 0 356 52" aria-hidden="true">
      <defs>
        <linearGradient id="tabFill" x1="0" y1="0" x2="0" y2="1">
          <stop offset="0" stop-color="var(--tab-top)"/>
          <stop offset="1" stop-color="var(--tab-bottom)"/>
        </linearGradient>
      </defs>
      <path d="M0,2 H356 L350,10 V42 Q350,50 342,50 H14 Q6,50 6,42 V10 Z" fill="url(#tabFill)"/>
      <circle cx="52" cy="28" r="15" fill="#1b6fae" stroke="#9fd9f7" stroke-width="2"/>
      <path d="M48,19 q-6,9 0,18 l4,-2 -2,-4 -2,1 q-2,-4 0,-8 l2,1 2,-4 z" fill="var(--white)"/>
    </svg>
    <p class="cta-label">CALL-TO-ACTION</p>

    <h2 class="treat-title">WITH PROPER TRAINING, YOU WILL BE ABLE TO TREAT:</h2>
    <ul class="conditions conditions-left">
      <li>Depression and other Affective Disorders</li>
      <li>Childhood Behavioral and Emotional Disorders</li>
      <li>Marital and Relationship Problems</li>
      <li>Conduct Disorder and Delinquency</li>
      <li>Substance Abuse</li>
    </ul>
    <ul class="conditions conditions-right">
      <li>Alcoholism</li>
      <li>Domestic Violence</li>
      <li>Severe Mental Illness</li>
      <li>Physical Illness</li>
    </ul>

    <svg class="tail" width="92" height="80" viewBox="0 0 92 80" aria-hidden="true">
      <polygon points="0,0 70,0 0,58" fill="var(--pink)"/>
      <polygon points="0,58 70,0 92,80" fill="var(--pink-dark)"/>
    </svg>

    <p class="aid-note">You could also qualify for financial aid*<br>from the government to pursue this career.<br>Secure your life by earning upto <strong>$78,580*</strong><br>and attain peace of mind while helping others.</p>
    <p class="brand">StudyHarbor</p>
  </div>
</div>
</body>
</html>
```